LAMBERTINE KOVAX Vaporizer Company Thoughtful Kovax for a brighter daily path.

I need a logo design for a new Colorado based company. We wholesale exclusive vaporizer units. Smoke inhalation delivers damaging carcinogens and an onslaught of other damaging materials directly through the bronchial tree and into the lungs.What this means in more simple terms is that the vaporizer completely eliminates every last chemical that is directly associated with burning of the material.

It Company

```html
<!DOCTYPE html>
<html lang="en">
<head>
<meta charset="UTF-8">
<title>Lambertine Kovax – Business Card</title>
<link href="https://fonts.googleapis.com/css2?family=Source+Sans+3:wght@400;600&display=swap" rel="stylesheet">
<style>
  :root {
    --backdrop: #2b2b2b;
    --card-white: #ffffff;
    --card-dark: #111111;
    --accent-green: #8ed11f;
    --accent-green-deep: #3f9e17;
    --ink-grey: #555555;
    --ink-light: #f2f2f2;
  }
  * { box-sizing: border-box; margin: 0; padding: 0; }
  html, body {
    width: 1200px;
    height: 599px;
    overflow: hidden;
  }
  body {
    background: var(--backdrop);
    font-family: "Source Sans 3", sans-serif;
    position: relative;
  }
  .card {
    position: absolute;
    top: 150px;
    width: 540px;
    height: 300px;
    border-radius: 22px;
    overflow: hidden;
    background: var(--card-white);
    box-shadow: 0 10px 24px rgba(0,0,0,0.45);
  }
  .card--front { left: 40px; }
  .card--back  { left: 620px; }

  .brand {
    display: flex;
    align-items: center;
    justify-content: center;
    gap: 12px;
  }
  .brand__dot {
    width: 26px;
    height: 26px;
    border-radius: 50%;
    background: var(--accent-green);
  }
  .brand__name {
    font-weight: 400;
    font-size: 30px;
    letter-spacing: 1px;
    color: var(--ink-grey);
  }

  .card--front .brand {
    position: absolute;
    top: 0; left: 0; right: 0;
    height: 190px;
  }
  .front__stripe {
    position: absolute;
    top: 186px; left: 0; right: 0;
    height: 6px;
    background: linear-gradient(to right, var(--accent-green-deep), var(--accent-green));
  }
  .front__panel {
    position: absolute;
    top: 192px; left: 0; right: 0; bottom: 0;
    background: var(--card-dark);
    color: var(--ink-light);
  }
  .holder {
    position: absolute;
    left: 30px; top: 14px;
    font-size: 19px;
    font-weight: 600;
  }
  .holder__role {
    font-weight: 400;
    color: var(--accent-green);
  }
  .holder__divider {
    font-weight: 400;
    color: var(--accent-green);
    margin: 0 4px;
  }
  .contact {
    position: absolute;
    left: 30px; top: 54px;
    list-style: none;
    font-size: 16px;
    line-height: 22px;
  }
  .contact li { display: flex; align-items: center; gap: 7px; }
  .contact svg { width: 14px; height: 14px; }
  .address {
    position: absolute;
    right: 26px; top: 12px;
    text-align: right;
    font-size: 16px;
    line-height: 21px;
    font-style: normal;
  }
  .address__line { display: flex; align-items: center; justify-content: flex-end; gap: 5px; }
  .address svg { width: 12px; height: 16px; }

  .card--back .brand {
    position: absolute;
    top: 110px; left: 0; right: 0;
  }
  .back__web {
    position: absolute;
    left: 0; right: 0; bottom: 34px;
    text-align: center;
    font-size: 17px;
    letter-spacing: 4px;
    color: #222222;
  }
</style>
</head>
<body>

  <section class="card card--front">
    <div class="brand">
      <span class="brand__dot"></span>
      <span class="brand__name">LAMBERTINE KOVAX</span>
    </div>
    <div class="front__stripe"></div>
    <div class="front__panel">
      <p class="holder">Firstname Lastname<span class="holder__divider">|</span><span class="holder__role">Director</span></p>
      <ul class="contact">
        <li>
          <svg viewBox="0 0 14 14" aria-hidden="true"><rect x="3" y="0.8" width="8" height="12.4" rx="1.5" fill="none" stroke="#f2f2f2" stroke-width="1.4"/><line x1="6" y1="10.8" x2="8" y2="10.8" stroke="#f2f2f2" stroke-width="1.2"/></svg>
          000 000 0000
        </li>
        <li>
          <svg viewBox="0 0 14 14" aria-hidden="true"><rect x="1" y="3" width="12" height="8.5" fill="none" stroke="#f2f2f2" stroke-width="1.3"/><polyline points="1,3 7,8 13,3" fill="none" stroke="#f2f2f2" stroke-width="1.3"/></svg>
          info@domainname.com
        </li>
      </ul>
      <address class="address">
        <span class="address__line">Adressline1,
          <svg viewBox="0 0 12 16" aria-hidden="true"><path d="M6 1a4.6 4.6 0 0 0-4.6 4.6C1.4 9.2 6 15 6 15s4.6-5.8 4.6-9.4A4.6 4.6 0 0 0 6 1z" fill="none" stroke="#f2f2f2" stroke-width="1.4"/><circle cx="6" cy="5.6" r="1.6" fill="#f2f2f2"/></svg>
        </span>
        <span class="address__line">Adressline2,</span>
        <span class="address__line">City</span>
      </address>
    </div>
  </section>

  <section class="card card--back">
    <div class="brand">
      <span class="brand__dot"></span>
      <span class="brand__name">LAMBERTINE KOVAX</span>
    </div>
    <p class="back__web">www.domainname.com</p>
  </section>

</body>
</html>
```